Commercial and Multifamily informational website

We need a website for our commercial real estate management company. We will manage offices, retail, apartments and others. Here is the brief verbiage: Providing quality commercial and multifamily portfolio management to Landlords, REITs, and financial institutions. 

Industry/Entity Type

Real Estate

Number of Pages Required

2 page

Font styles to use
Sans Serif
Other font styles liked:
• Muli, Garamond

Colors
0555a3
5c5c5c
3176b5
85acd3
474747

Requirements
Must have
• Home page and contact page

```html
<!DOCTYPE html>
<html lang="en">
<head>
<meta charset="utf-8">
<title>Halden Property Management</title>
<link rel="stylesheet" href="https://fonts.googleapis.com/css2?family=Mulish:ital,wght@0,400;0,600;0,700;0,800;1,400&family=EB+Garamond:wght@400;500;600&display=swap">
<style>
:root{
  --blue:#0555a3;
  --mid-blue:#3176b5;
  --soft-blue:#85acd3;
  --gray:#5c5c5c;
  --dark:#474747;
  --footer:#2a2a2a;
  --footer-deep:#1c1c1c;
  --paper:#ffffff;
  --mist:#f1f1f1;
  --rule:#d8d8d8;
}
*{box-sizing:border-box;margin:0;padding:0}
html,body{width:1200px;height:2464px;overflow:hidden}
body{font-family:"Mulish",Arial,sans-serif;color:var(--gray);background:var(--paper);font-size:15px;line-height:1.6}
.wrap{width:1060px;margin:0 auto;position:relative;height:100%}
a{color:inherit;text-decoration:none}

/* top bar */
.topbar{height:32px;background:var(--blue);color:#fff;font-size:13px}
.topbar .wrap{display:flex;justify-content:flex-end;align-items:center;gap:34px}
.topbar span{display:flex;align-items:center;gap:8px}
.topbar .phone{font-weight:700;font-size:15px}

/* header */
.site-header{height:108px;background:var(--paper);border-bottom:1px solid var(--rule)}
.site-header .wrap{display:flex;align-items:center;justify-content:space-between}
.brand{display:flex;align-items:center;gap:14px;color:var(--blue);font-weight:800;font-size:26px;line-height:1.05;letter-spacing:.5px}
.brand-mark{width:46px;height:46px;background:var(--blue)}
.main-nav{display:flex;gap:6px;align-self:flex-start;margin-top:14px}
.main-nav a{font-size:14px;font-weight:600;color:var(--dark);padding:10px 20px;border-right:1px solid var(--rule)}
.main-nav a:last-child{border-right:0}
.main-nav a.active{color:var(--mid-blue)}

/* hero */
.hero{height:460px;position:relative;overflow:hidden}
.hero-photo{position:absolute;inset:0;background:linear-gradient(100deg,#1d2a36 0%,#48525b 28%,#b8bec4 52%,#7d8790 75%,#3b4650 100%)}
.hero-copy{position:absolute;right:0;top:150px;width:640px;background:rgba(5,85,163,.85);color:#fff;padding:24px 70px 24px 40px;font-weight:800;font-size:24px;line-height:1.3;letter-spacing:.4px;text-align:right}
.hero-cta{position:absolute;right:70px;top:312px;background:#111;color:#fff;font-weight:700;font-size:15px;padding:12px 26px}
.hero-dots{position:absolute;right:80px;bottom:26px;display:flex;gap:8px}
.hero-dots i{width:12px;height:12px;border-radius:50%;border:2px solid #fff;display:block}
.hero-dots i.on{background:#fff}

/* headings */
.section-title{font-family:"EB Garamond",Georgia,serif;font-size:40px;font-weight:500;color:var(--dark);text-align:center;letter-spacing:1px;text-transform:uppercase}
.section-title strong{color:var(--blue);font-weight:600}
.title-rule{width:560px;height:1px;background:var(--rule);margin:12px auto 0;position:relative}
.title-rule:after{content:"";position:absolute;left:50%;top:-2px;width:90px;margin-left:-45px;height:4px;background:var(--blue)}

/* welcome */
.welcome{height:600px;padding-top:46px}
.welcome p{width:1000px;margin:28px auto 0;font-size:14px;line-height:1.75}
.tablet{width:520px;height:300px;margin:44px auto 0;background:#111;border-radius:22px;padding:20px 34px;position:relative}
.tablet-screen{width:100%;height:100%;background:linear-gradient(160deg,#c9dcef 0%,#6f93b8 45%,#2e4f73 100%);position:relative}
.play{position:absolute;left:50%;top:50%;width:70px;height:70px;margin:-35px 0 0 -35px}

/* services */
.services{height:500px;border-top:1px solid var(--rule);padding-top:40px;position:relative}
.services .lede{width:560px;margin:22px auto 0;text-align:center;font-size:13px;line-height:1.6}
.service-row{display:flex;justify-content:space-between;width:940px;margin:40px auto 0}
.service{width:260px;text-align:center}
.service h3{font-family:"EB Garamond",Georgia,serif;font-size:26px;font-weight:600;color:var(--dark);letter-spacing:1px;border-bottom:1px solid var(--rule);padding-bottom:6px}
.service.featured h3{color:var(--mid-blue)}
.service-icon{width:120px;height:120px;background:var(--dark);margin:24px auto 22px;display:flex;align-items:center;justify-content:center}
.service.featured .service-icon{background:var(--blue)}
.service p{font-size:14px;line-height:1.6;color:var(--dark)}
.read-more{display:inline-block;margin-top:6px;font-size:13px;color:var(--mid-blue)}
.arrow{position:absolute;top:268px;width:36px;height:36px;border-radius:50%;border:1px solid #bbb;background:#fff;display:flex;align-items:center;justify-content:center}
.arrow.left{left:40px}
.arrow.right{right:40px}

/* testimonials */
.testimonials{height:420px;background:var(--mist);padding-top:40px;position:relative}
.quote-row{display:flex;justify-content:space-between;width:1000px;margin:46px auto 0}
.quote{width:470px;display:flex;gap:24px}
.portrait{width:140px;height:140px;border-radius:50%;flex:none;background:radial-gradient(circle at 50% 40%,#d8c2ad,#8a7868 70%,#5f5a56)}
.portrait.alt{background:radial-gradient(circle at 50% 40%,#e6e0da,#a8a29c 70%,#6e6b68)}
.quote blockquote{font-style:italic;font-size:14px;line-height:1.65;color:var(--gray);position:relative;padding:0 0 0 24px}
.quote blockquote:before{content:"\201C";position:absolute;left:0;top:-8px;font-size:36px;color:var(--mid-blue);font-style:normal}
.stars{color:var(--mid-blue);font-size:18px;letter-spacing:2px;margin:8px 0 0 24px}
.quote-name{font-family:"EB Garamond",Georgia,serif;font-weight:600;color:var(--blue);font-size:18px;letter-spacing:1px;text-transform:uppercase;margin-top:14px;width:470px}
.quote-name.right{text-align:right}
.pager{position:absolute;left:50%;bottom:28px;margin-left:-36px;display:flex;gap:12px}
.pager span{width:30px;height:30px;border-radius:50%;background:#fff;border:1px solid #ccc;display:flex;align-items:center;justify-content:center}

/* footer */
.site-footer{height:300px;background:var(--footer);color:#cfcfcf;padding-top:44px;font-size:13px}
.site-footer .wrap{display:flex;gap:50px}
.site-footer h4{color:#fff;font-size:15px;font-weight:700;margin-bottom:16px}
.quick-links{width:140px}
.quick-links li{list-style:none;line-height:2.1;padding-left:14px;position:relative}
.quick-links li:before{content:"";position:absolute;left:0;top:13px;width:5px;height:5px;background:var(--soft-blue)}
.contact-info{width:230px;line-height:1.8}
.contact-info .line{display:flex;gap:10px;align-items:center;margin-top:6px}
.map-block{width:260px}
.map{width:260px;height:170px;background:linear-gradient(135deg,#e4e1d6,#c9d8c4 50%,#b9cfe0)}
.footer-brand{flex:1;display:flex;flex-direction:column;align-items:flex-end;justify-content:center;gap:26px;padding-top:20px}
.footer-brand .brand{color:#fff;font-size:24px}
.footer-brand .brand-mark{background:#fff}
.social{display:flex;gap:10px}
.social i{width:30px;height:30px;border-radius:50%;background:var(--mid-blue);display:block}
.copyright{height:44px;background:var(--footer-deep);color:#9a9a9a;font-size:12px;display:flex;align-items:center}
</style>
</head>
<body>

<div class="topbar">
  <div class="wrap">
    <span><svg width="16" height="12" viewBox="0 0 16 12"><rect x="0.5" y="0.5" width="15" height="11" fill="none" stroke="#fff"/><path d="M1 1l7 6 7-6" fill="none" stroke="#fff"/></svg>info@haldenpm.com</span>
    <span class="phone"><svg width="14" height="14" viewBox="0 0 14 14"><path d="M3 1l2.5 3-1.5 1.5c.8 1.8 2.2 3.2 4 4L9.5 8 13 10.5 11.5 13C6 13 1 8 1 2.5z" fill="#fff"/></svg>(+012) 555 0148</span>
  </div>
</div>

<header class="site-header">
  <div class="wrap">
    <div class="brand"><span class="brand-mark"></span><span>HALDEN PROPERTY<br>MANAGEMENT</span></div>
    <nav class="main-nav">
      <a href="#" class="active">HOME</a>
      <a href="#">ABOUT US</a>
      <a href="#">SERVICES</a>
      <a href="#">CONTACT US</a>
    </nav>
  </div>
</header>

<section class="hero">
  <div class="hero-photo" role="img" aria-label="Photo of two businessmen in suits shaking hands"></div>
  <div class="hero-copy">PROVIDING QUALITY COMMERCIAL AND MULTIFAMILY PORTFOLIO MANAGEMENT TO LANDLORDS, REITS, AND FINANCIAL INSTITUTIONS</div>
  <a class="hero-cta" href="#">REQUEST A QUOTE</a>
  <div class="hero-dots"><i class="on"></i><i></i><i></i><i></i></div>
</section>

<section class="welcome">
  <h2 class="section-title">Welcome to <strong>Halden Property Management</strong></h2>
  <div class="title-rule"></div>
  <p>Lorem Ipsum is simply dummy text of the printing and typesetting industry. Lorem Ipsum has been the industry's standard dummy text ever since the 1500s, when an unknown printer took a galley of type and scrambled it to make a type specimen book. It has survived not only five centuries, but also the leap into electronic typesetting, remaining essentially unchanged. It was popularised in the 1960s with the release [+].</p>
  <div class="tablet">
    <div class="tablet-screen" role="img" aria-label="Video still of a glass office tower against a blue sky">
      <svg class="play" viewBox="0 0 70 70"><circle cx="35" cy="35" r="33" fill="rgba(0,0,0,.45)" stroke="#fff" stroke-width="3"/><path d="M28 22l20 13-20 13z" fill="#fff"/></svg>
    </div>
  </div>
</section>

<section class="services">
  <h2 class="section-title">Our <strong>Services</strong></h2>
  <div class="title-rule"></div>
  <p class="lede">Lorem Ipsum is simply dummy text of the printing and typesetting industry. Lorem Ipsum has been the industry's standard dummy text ever since the 1500s.</p>
  <div class="service-row">
    <div class="service">
      <h3>OFFICES</h3>
      <div class="service-icon"><svg width="56" height="56" viewBox="0 0 56 56"><rect x="8" y="6" width="28" height="46" fill="#fff"/><rect x="36" y="22" width="14" height="30" fill="#fff"/><g fill="#474747"><rect x="13" y="12" width="6" height="6"/><rect x="25" y="12" width="6" height="6"/><rect x="13" y="24" width="6" height="6"/><rect x="25" y="24" width="6" height="6"/><rect x="13" y="36" width="6" height="6"/><rect x="25" y="36" width="6" height="6"/><rect x="40" y="28" width="6" height="5"/><rect x="40" y="38" width="6" height="5"/></g></svg></div>
      <p>Lorem Ipsum is simply text of the printing and typesetting industry. Lorem Ipsum has been indus...</p>
      <a class="read-more" href="#">Read More</a>
    </div>
    <div class="service featured">
      <h3>RETAIL</h3>
      <div class="service-icon"><svg width="56" height="56" viewBox="0 0 56 56"><path d="M6 10h44l-3 12H9z" fill="#fff"/><rect x="10" y="24" width="36" height="26" fill="#fff"/><rect x="20" y="32" width="16" height="18" fill="#0555a3"/></svg></div>
      <p>Lorem Ipsum is simply text of the printing and typesetting industry. Lorem Ipsum has been indus...</p>
      <a class="read-more" href="#">Read More</a>
    </div>
    <div class="service">
      <h3>APARTMENTS</h3>
      <div class="service-icon"><svg width="56" height="56" viewBox="0 0 56 56"><rect x="10" y="6" width="36" height="46" fill="#fff"/><g fill="#474747"><rect x="16" y="12" width="8" height="7"/><rect x="32" y="12" width="8" height="7"/><rect x="16" y="24" width="8" height="7"/><rect x="32" y="24" width="8" height="7"/><rect x="24" y="38" width="8" height="14"/></g></svg></div>
      <p>Lorem Ipsum is simply text of the printing and typesetting industry. Lorem Ipsum has been indus...</p>
      <a class="read-more" href="#">Read More</a>
    </div>
  </div>
  <span class="arrow left"><svg width="12" height="12" viewBox="0 0 12 12"><path d="M8 1L3 6l5 5" fill="none" stroke="#474747" stroke-width="2"/></svg></span>
  <span class="arrow right"><svg width="12" height="12" viewBox="0 0 12 12"><path d="M4 1l5 5-5 5" fill="none" stroke="#474747" stroke-width="2"/></svg></span>
</section>

<section class="testimonials">
  <h2 class="section-title">Client <strong>Testimonials</strong></h2>
  <div class="title-rule"></div>
  <div class="quote-row">
    <div>
      <div class="quote">
        <div class="portrait" role="img" aria-label="Portrait photo of a smiling male client"></div>
        <div>
          <blockquote>Their team took over our retail portfolio and the change was clear within months. Reporting is prompt, tenants are happier and costs are finally under control.</blockquote>
          <div class="stars">★★★★★</div>
        </div>
      </div>
      <div class="quote-name">Mr. Paul Brennan</div>
    </div>
    <div>
      <div class="quote">
        <div class="portrait alt" role="img" aria-label="Portrait photo of a client"></div>
        <div>
          <blockquote>We trust them with three apartment buildings. Every request gets a quick answer, vacancies are filled fast and the monthly statements are easy to read.</blockquote>
          <div class="stars">★★★★★</div>
        </div>
      </div>
      <div class="quote-name right">Mrs. Clara Brennan</div>
    </div>
  </div>
  <div class="pager">
    <span><svg width="10" height="10" viewBox="0 0 10 10"><path d="M7 1L3 5l4 4" fill="none" stroke="#474747" stroke-width="2"/></svg></span>
    <span><svg width="10" height="10" viewBox="0 0 10 10"><path d="M3 1l4 4-4 4" fill="none" stroke="#474747" stroke-width="2"/></svg></span>
  </div>
</section>

<footer class="site-footer">
  <div class="wrap">
    <div class="quick-links">
      <h4>Quick Links</h4>
      <ul><li>Home</li><li>About Us</li><li>Services</li><li>Contact Us</li></ul>
    </div>
    <div class="contact-info">
      <h4>Contact Information</h4>
      <div>Halden Property Management<br>24 Harbor Row, Suite 310<br>Westfield, NY 10021</div>
      <div class="line"><svg width="12" height="12" viewBox="0 0 14 14"><path d="M3 1l2.5 3-1.5 1.5c.8 1.8 2.2 3.2 4 4L9.5 8 13 10.5 11.5 13C6 13 1 8 1 2.5z" fill="#85acd3"/></svg>(+012) 555 0148</div>
      <div class="line"><svg width="14" height="10" viewBox="0 0 16 12"><rect x="0.5" y="0.5" width="15" height="11" fill="none" stroke="#85acd3"/><path d="M1 1l7 6 7-6" fill="none" stroke="#85acd3"/></svg>info@haldenpm.com</div>
    </div>
    <div class="map-block">
      <h4>Location Map</h4>
      <div class="map" role="img" aria-label="Street map showing the office location"></div>
    </div>
    <div class="footer-brand">
      <div class="brand"><span class="brand-mark"></span><span>HALDEN PROPERTY<br>MANAGEMENT</span></div>
      <div class="social"><i></i><i></i><i></i><i></i></div>
    </div>
  </div>
</footer>

<div class="copyright"><div class="wrap" style="display:flex;align-items:center">© Copyright 2017. All Rights Reserved Halden Property Management</div></div>

</body>
</html>
```